Fahrzeugbeschriftung für eine  Autofahrschule
Fahrzeugbeschriftung für eine Autofahrschule
Zielgruppe
Autofahrschule, 18jährige +, also eher junge Leute, die ihren Führerschein machen wollen
Aufgabenstellung
D/E/F bitte bei neuen Vorschlägen weglassen, da es mir nicht so gut gefällt, wenn auf dem Fahrzeug vermerkt.
Worauf legen Sie bei Ihrem Design besonderen Wert? Modernes und anspruchsvolles Design, nicht übertrieben gross, unter Berücksichtigung bereits vorhandenem Design auf dem Fahrzeug, aber nicht zwingend (ausser ,,Rudel K''
Welchen Text möchten Sie in Ihrem Design? ,,kolbeck's fahrschule'' oder ,,Kolbeck's Fahrschule''
,,deutsch/englisch/französisch''
Das Fahrzeug ist ein Brenta Q70, T-Linie, schwarz und hat bereits ein Design in blau. Dieses Design kann übernommen und ergänzt werden, oder ersetzt werden. Hingegen sollte das Logo ,,Rudel K'' bleiben wo es ist (C-Säule links und rechts, siehe Fotos)

```html
<!DOCTYPE html>
<html lang="de">
<head>
<meta charset="utf-8">
<title>Beschriftungs Beispiele – Kolbeck´s Fahrschule</title>
<link rel="stylesheet" href="https://fonts.googleapis.com/css2?family=Kalam:wght@700&family=Delius&family=Italianno&family=Poiret+One&family=Cinzel:wght@600&family=Cormorant+Garamond:wght@500&family=Oswald:wght@500&family=Cousine&family=Princess+Sofia&family=Alegreya&family=Mali:wght@500&display=swap">
<style>
  :root {
    --bg: #333333;
    --ink: #ffffff;
    --rule: #d9d9d9;
    --pill: #2c5a86;
    --pill-ink: #a9d2f5;
  }
  * { margin: 0; padding: 0; box-sizing: border-box; }
  html, body { width: 929px; height: 1200px; overflow: hidden; background: var(--bg); }
  .sheet { position: relative; width: 929px; height: 1200px; background: var(--bg); color: var(--ink); }

  .sheet-title {
    position: absolute; left: 223px; top: 42px; width: 416px; height: 34px;
    background: var(--pill); border-radius: 17px;
    font-family: "Kalam", cursive; font-weight: 700; font-size: 30px; line-height: 36px;
    color: var(--pill-ink); text-align: center; letter-spacing: 1px;
  }

  .rule { position: absolute; background: var(--rule); }
  .rule--v { width: 1px; }
  .rule--h { height: 1px; }

  .line { position: absolute; white-space: nowrap; line-height: 1; }

  /* Variante 1 */
  .v1-name { left: 57px; top: 247px; font-family: "Delius", cursive; font-size: 32px; }
  .v1-tel { left: 49px; top: 350px; font-family: Arial, Helvetica, sans-serif; font-size: 22px; }

  /* Variante 2 */
  .v2-name { left: 512px; top: 220px; font-family: "Italianno", cursive; font-size: 56px; }
  .v2-tel { left: 510px; top: 333px; font-family: "Poiret One", sans-serif; font-size: 27px; font-weight: 700; }

  /* Variante 3 */
  .v3-name { left: 39px; top: 525px; font-family: "Cinzel", serif; font-weight: 600; font-size: 27px; letter-spacing: 2px; }
  .v3-tel { left: 42px; top: 629px; font-family: "Cormorant Garamond", serif; font-weight: 500; font-size: 20px; font-variant-numeric: lining-nums; }

  /* Variante 4 */
  .v4-name { left: 518px; top: 500px; font-family: "Oswald", sans-serif; font-weight: 500; font-size: 31px; }
  .v4-tel { left: 519px; top: 611px; font-family: "Cousine", monospace; font-size: 17px; }
  .v4-tel .label { font-family: Arial, Helvetica, sans-serif; font-size: 18px; }

  /* Variante 5 */
  .v5-name { left: 47px; top: 794px; font-family: "Princess Sofia", cursive; font-size: 36px; }
  .v5-tel { left: 52px; top: 935px; font-family: "Alegreya", serif; font-size: 26px; font-variant-numeric: lining-nums; }

  /* Variante 6 */
  .v6-name { left: 516px; top: 803px; font-family: "Mali", cursive; font-weight: 500; font-size: 34px; }
  .v6-tel { left: 513px; top: 961px; font-family: Arial, Helvetica, sans-serif; font-size: 23px; }
</style>
</head>
<body>
<main class="sheet">
  <h1 class="sheet-title">Beschriftungs Beispiele:</h1>

  <div class="rule rule--v" style="left:473px; top:191px; height:224px;"></div>
  <div class="rule rule--h" style="left:25px; top:414px; width:899px;"></div>
  <div class="rule rule--v" style="left:476px; top:414px; height:299px;"></div>
  <div class="rule rule--h" style="left:26px; top:713px; width:898px;"></div>
  <div class="rule rule--v" style="left:479px; top:713px; height:309px;"></div>

  <section class="variant">
    <p class="line v1-name">Kolbeck´s Fahrschule</p>
    <p class="line v1-tel">Tel. 077 318 52 46</p>
  </section>

  <section class="variant">
    <p class="line v2-name">Kolbeck´s Fahrschule</p>
    <p class="line v2-tel">Tel. 077 318 52 46</p>
  </section>

  <section class="variant">
    <p class="line v3-name">Kolbeck´s Fahrschule</p>
    <p class="line v3-tel">Tel. 077 318 52 46</p>
  </section>

  <section class="variant">
    <p class="line v4-name">Kolbeck´s Fahrschule</p>
    <p class="line v4-tel"><span class="label">Tel.</span> 077 318 52 46</p>
  </section>

  <section class="variant">
    <p class="line v5-name">Kolbeck´s Fahrschule</p>
    <p class="line v5-tel">Tel. 077 318 52 46</p>
  </section>

  <section class="variant">
    <p class="line v6-name">Kolbeck´s Fahrschule</p>
    <p class="line v6-tel">Tel. 077 318 52 46</p>
  </section>
</main>
</body>
</html>
```